Anzeigengestaltung für Heilpraktikerin für Psychotherapie
Hallo lorvik, ich bin sehr zufrieden mit dem Design. Danke LG Helga Brandner
Zielgruppe
Heilpraktikerin für Psychotherapie, Atem- und Körpertherapeutin, Einzelthearpie, Gruppentherapie, Menschen in Lebenskrisen; Menschen, die ihr Leben verändern wollen, Menschen suchen mehr Selbsterfahrung, vorwiegend Frauen, Atersgruppe 20 aufwärts, Menschen mit psychischen Problemen
Entspannung, Berühren, Massieren, Halten, Gespräch, Bewegen, Begleitung Während der Schwangerschaft, Geburt und danach, Trauerbegleitung
Aufgabenstellung
Name und Berufsbezeichnung sind mir wichtig
Praxiseröffnung, Termine nach Vereinbarung
aktuelles Angebot: Fantasiereise- Entspannung von Alltagsstress
sonstiges Angebot: Einzeltherapie/Gruppentherapie,

```html
<!DOCTYPE html>
<html lang="de">
<head>
<meta charset="utf-8">
<title>Lichtraum – Anzeigen Praxiseröffnung</title>
<link rel="stylesheet" href="https://fonts.googleapis.com/css2?family=Montserrat:wght@500;600;700&family=Permanent+Marker&display=swap">
<style>
  :root {
    --plum: #6d2a52;
    --magenta: #e0007a;
    --coral: #f28a78;
    --white: #ffffff;
    --backdrop: #ece7e4;
    --ink: #6d2a52;
  }
  * { box-sizing: border-box; margin: 0; padding: 0; }
  html, body { width: 1200px; height: 789px; overflow: hidden; }
  body {
    background: var(--backdrop);
    font-family: "Montserrat", Arial, sans-serif;
    color: var(--white);
    position: relative;
  }
  .ad { position: absolute; background: var(--white); overflow: hidden; }
  .abs { position: absolute; }
  .center { text-align: center; left: 0; right: 0; }

  .brand-name {
    font-weight: 600;
    color: var(--ink);
    letter-spacing: 0.02em;
    display: flex; align-items: center; justify-content: center; gap: 8px;
  }
  .brand-dot { border-radius: 50%; background: var(--ink); display: inline-block; }

  .headline { font-weight: 600; letter-spacing: 0.08em; }
  .person { font-weight: 600; }
  .role, .address { font-weight: 600; }
  .hours { font-weight: 700; }
  .phone, .web { font-weight: 700; letter-spacing: 0.03em; }

  .services { list-style: none; font-weight: 600; }
  .services li { position: relative; padding-left: 10px; }
  .services li::before { content: "•"; position: absolute; left: 0; }

  .sticker { position: absolute; }
  .sticker svg { display: block; overflow: visible; }
  .sticker-kicker { font-family: "Permanent Marker", "Montserrat", sans-serif; font-size: 12.5px; fill: var(--white); letter-spacing: 0.02em; }
  .sticker-title { font-family: "Montserrat", Arial, sans-serif; font-weight: 700; font-size: 15px; fill: var(--white); }
  .sticker-sub { font-family: "Montserrat", Arial, sans-serif; font-weight: 600; font-size: 8.6px; fill: var(--white); }
  .sticker-swoosh { stroke: var(--white); stroke-width: 2.6; fill: none; stroke-linecap: round; }
  .sticker-peel-back { fill: var(--plum); }
  .sticker-peel { fill: var(--white); }

  /* Hochformat-Anzeige */
  .ad-portrait { left: 361px; top: 140px; width: 248px; height: 510px; }
  .ad-portrait .plum-field { left: 0; top: 163px; width: 248px; height: 347px; background: var(--plum); }
  .ad-portrait .band { left: 12px; top: 141px; width: 224px; height: 22px; }
  .ad-portrait .brand-name { top: 98px; font-size: 27px; }
  .ad-portrait .brand-dot { width: 10px; height: 10px; }
  .ad-portrait .headline { top: 176px; font-size: 18px; }
  .ad-portrait .person { top: 202px; font-size: 13px; }
  .ad-portrait .role { top: 219px; font-size: 11px; }
  .ad-portrait .address { top: 236px; font-size: 11px; }
  .ad-portrait .sticker { left: -2px; top: 255px; width: 130px; height: 132px; }
  .ad-portrait .services { font-size: 11.5px; line-height: 1.3; }
  .ad-portrait .hours { top: 426px; font-size: 14px; }
  .ad-portrait .phone { top: 453px; font-size: 17px; }
  .ad-portrait .web { top: 476px; font-size: 15px; }

  /* Querformat-Anzeige */
  .ad-landscape { left: 662px; top: 311px; width: 512px; height: 368px; }
  .ad-landscape .plum-left { left: 0; top: 180px; width: 293px; height: 188px; background: var(--plum); }
  .ad-landscape .plum-right { left: 301px; top: 0; width: 211px; height: 368px; background: var(--plum); }
  .ad-landscape .band { left: 22px; top: 157px; width: 251px; height: 23px; }
  .ad-landscape .brand-name { left: 0; width: 301px; top: 112px; font-size: 31px; }
  .ad-landscape .brand-dot { width: 11px; height: 11px; }
  .ad-landscape .left-text { left: 0; width: 293px; }
  .ad-landscape .headline { top: 190px; font-size: 21px; }
  .ad-landscape .person { top: 222px; font-size: 15px; }
  .ad-landscape .role { top: 243px; font-size: 12.5px; }
  .ad-landscape .address { top: 263px; font-size: 12.5px; }
  .ad-landscape .hours { top: 290px; font-size: 14.5px; }
  .ad-landscape .phone { top: 318px; font-size: 17px; }
  .ad-landscape .web { top: 340px; font-size: 15px; }
  .ad-landscape .sticker { left: 323px; top: 16px; width: 166px; height: 168px; }
  .ad-landscape .services { left: 330px; top: 190px; font-size: 14.5px; line-height: 1.3; }
  .ad-landscape .services li { margin-bottom: 8px; }
</style>
</head>
<body>

<!-- Hochformat -->
<article class="ad ad-portrait">
  <div class="abs center brand-name"><span class="brand-dot"></span>Lichtraum</div>
  <svg class="abs band" viewBox="0 0 224 22" preserveAspectRatio="none" aria-hidden="true">
    <path d="M0 0 Q112 16 224 0 V22 H0 Z" fill="#e0007a"/>
  </svg>
  <div class="abs plum-field"></div>
  <h1 class="abs center headline">PRAXISERÖFFNUNG</h1>
  <p class="abs center person">Helga Brandner</p>
  <p class="abs center role">Heilpraktikerin für Psychotherapie</p>
  <p class="abs center address">72581 Lindach • Gartenweg 14</p>

  <div class="sticker">
    <svg width="130" height="132" viewBox="0 0 130 132">
      <defs>
        <linearGradient id="stickerFillP" x1="0" y1="0" x2="0" y2="1">
          <stop offset="0.35" stop-color="#e0007a"/>
          <stop offset="1" stop-color="#f28a78"/>
        </linearGradient>
      </defs>
      <circle cx="64" cy="68" r="62" fill="url(#stickerFillP)" stroke="#ffffff" stroke-width="1"/>
      <path class="sticker-peel-back" d="M12 30 Q60 20 96 6 Q110 14 116 26 Q80 40 12 30 Z"/>
      <path class="sticker-peel" d="M14 27 Q62 30 96 6 Q100 20 90 24 Q52 36 14 27 Z"/>
      <g transform="rotate(-8 64 68)">
        <text class="sticker-kicker" x="62" y="49" text-anchor="middle">MEIN ANGEBOT</text>
        <path class="sticker-swoosh" d="M20 60 Q64 53 112 54"/>
        <text class="sticker-title" x="64" y="79" text-anchor="middle">Fantasiereise</text>
        <text class="sticker-sub" x="64" y="91" text-anchor="middle">Entspannung vom</text>
        <text class="sticker-sub" x="66" y="101" text-anchor="middle">Alltagsstress</text>
      </g>
    </svg>
  </div>

  <ul class="abs services">
    <li style="position:absolute;left:134px;top:302px;width:120px">Atem- und<br>Körpertherapie</li>
    <li style="position:absolute;left:128px;top:349px;width:130px">Psychotherapie</li>
    <li style="position:absolute;left:110px;top:374px;width:140px">Krisenbewältigung</li>
    <li style="position:absolute;left:44px;top:396px;width:210px">Einzel- und Gruppentherapie</li>
  </ul>

  <p class="abs center hours">Termine nach Vereinbarung</p>
  <p class="abs center phone">01579 4382016</p>
  <p class="abs center web">www.lichtraum-praxis.de</p>
</article>

<!-- Querformat -->
<article class="ad ad-landscape">
  <div class="abs brand-name"><span class="brand-dot"></span>Lichtraum</div>
  <svg class="abs band" viewBox="0 0 251 23" preserveAspectRatio="none" aria-hidden="true">
    <path d="M0 0 Q125 16 251 0 V23 H0 Z" fill="#e0007a"/>
  </svg>
  <div class="abs plum-left"></div>
  <div class="abs plum-right"></div>

  <h1 class="abs left-text center headline" style="right:auto">PRAXISERÖFFNUNG</h1>
  <p class="abs left-text center person" style="right:auto">Helga Brandner</p>
  <p class="abs left-text center role" style="right:auto">Heilpraktikerin für Psychotherapie</p>
  <p class="abs left-text center address" style="right:auto">72581 Lindach • Gartenweg 14</p>
  <p class="abs left-text center hours" style="right:auto">Termine nach Vereinbarung</p>
  <p class="abs left-text center phone" style="right:auto">01579 4382016</p>
  <p class="abs left-text center web" style="right:auto">www.lichtraum-praxis.de</p>

  <div class="sticker">
    <svg width="166" height="168" viewBox="0 0 130 132">
      <defs>
        <linearGradient id="stickerFillL" x1="0" y1="0" x2="0" y2="1">
          <stop offset="0.35" stop-color="#e0007a"/>
          <stop offset="1" stop-color="#f28a78"/>
        </linearGradient>
      </defs>
      <circle cx="64" cy="68" r="62" fill="url(#stickerFillL)" stroke="#ffffff" stroke-width="1"/>
      <path class="sticker-peel-back" d="M12 30 Q60 20 96 6 Q110 14 116 26 Q80 40 12 30 Z"/>
      <path class="sticker-peel" d="M14 27 Q62 30 96 6 Q100 20 90 24 Q52 36 14 27 Z"/>
      <g transform="rotate(-8 64 68)">
        <text class="sticker-kicker" x="62" y="49" text-anchor="middle">MEIN ANGEBOT</text>
        <path class="sticker-swoosh" d="M20 60 Q64 53 112 54"/>
        <text class="sticker-title" x="64" y="79" text-anchor="middle">Fantasiereise</text>
        <text class="sticker-sub" x="64" y="91" text-anchor="middle">Entspannung vom</text>
        <text class="sticker-sub" x="66" y="101" text-anchor="middle">Alltagsstress</text>
      </g>
    </svg>
  </div>

  <ul class="abs services">
    <li>Atem- und<br>Körpertherapie</li>
    <li>Psychotherapie</li>
    <li>Krisenbewältigung</li>
    <li>Einzel- und<br>Gruppentherapie</li>
  </ul>
</article>

</body>
</html>
```